Business Card Design Project

Logo, Phone Number, slogan, must be included on front of card. Services must be listed: Lawn Service, Fertilization, Pool Service, Pressure Washing. and a space to "write in" salesmans name.
Slogan "Your Everything Outside Company"
Phone: 555-204-3816
Email: brightmeadowgroup@mailvane.com
Looking for a bold yet simple design to enforce brand recognition.

Target Market(s)

Middle to upper class US homeowners

Industry/Entity Type

Business

Requirements
Must have
• Logo, Phone, and Slogan on front
Should not have
• cluttered background

```html
<!DOCTYPE html>
<html lang="en">
<head>
<meta charset="utf-8">
<title>Bright Meadow Services – Business Card</title>
<link rel="stylesheet" href="https://fonts.googleapis.com/css2?family=Michroma&family=Open+Sans:wght@400;600&family=PT+Sans&display=swap">
<style>
  :root{
    --backdrop:#e9e9e6;
    --card:#ffffff;
    --navy:#1f5d8f;
    --slate:#5b6165;
    --lime:#8dc63f;
    --leaf:#5a8a3a;
    --forest:#4f7f2f;
    --ink-white:#ffffff;
  }
  *{margin:0;padding:0;box-sizing:border-box}
  html,body{width:1200px;height:930px;overflow:hidden;background:var(--backdrop)}
  .sheet{position:relative;width:1200px;height:930px}
  .card{
    position:absolute;left:232px;width:735px;height:420px;
    background:var(--card);overflow:hidden;
    box-shadow:0 6px 18px rgba(0,0,0,.12);
  }
  .card--front{top:30px}
  .card--back{top:480px}

  /* front */
  .brand{
    position:absolute;left:0;right:0;top:92px;
    display:flex;align-items:center;justify-content:center;gap:14px;
  }
  .brand__mark{width:22px;height:22px;border-radius:50%;background:var(--lime)}
  .brand__name{
    font-family:"Michroma",sans-serif;font-size:34px;color:var(--navy);
    letter-spacing:1px;line-height:1.15;text-align:center;
  }
  .slogan{
    position:absolute;left:130px;top:196px;
    font-family:"Michroma",sans-serif;font-size:16.5px;font-weight:400;
    color:var(--navy);letter-spacing:.5px;white-space:nowrap;
  }
  .front-band{position:absolute;left:0;top:226px;width:735px;height:72px}
  .grass{position:absolute;left:590px;top:210px;width:145px;height:88px}
  .phone{
    position:absolute;left:190px;top:316px;
    font-family:"PT Sans",sans-serif;font-size:30px;color:var(--navy);letter-spacing:.5px;
  }

  /* back */
  .signature-line{
    position:absolute;left:70px;top:118px;width:590px;height:0;
    border-top:2px dotted var(--forest);
  }
  .tagline{
    position:absolute;left:0;right:0;top:150px;text-align:center;
    font-family:"Open Sans",sans-serif;font-size:20px;color:var(--leaf);
  }
  .service-band{
    position:absolute;left:0;bottom:0;width:735px;height:140px;background:var(--leaf);
  }
  .service-list{
    position:absolute;top:28px;list-style:none;
    font-family:"Open Sans",sans-serif;font-size:23px;line-height:1.25;color:var(--ink-white);
  }
  .service-list--start{left:44px}
  .service-list--end{right:60px}
</style>
</head>
<body>
<main class="sheet">

  <section class="card card--front" aria-label="Card front">
    <div class="brand">
      <span class="brand__mark"></span>
      <span class="brand__name">BRIGHT MEADOW<br>SERVICES</span>
    </div>

    <svg class="front-band" viewBox="0 0 735 72" aria-hidden="true">
      <rect x="0" y="0" width="470" height="72" fill="var(--lime)"/>
      <rect x="470" y="4" width="40" height="64" fill="var(--forest)"/>
      <rect x="510" y="4" width="14" height="64" fill="var(--lime)"/>
      <rect x="524" y="4" width="18" height="64" fill="var(--forest)"/>
      <rect x="542" y="4" width="12" height="64" fill="var(--lime)"/>
      <rect x="554" y="4" width="12" height="64" fill="var(--forest)"/>
      <rect x="566" y="4" width="10" height="64" fill="var(--lime)"/>
      <rect x="576" y="4" width="159" height="64" fill="var(--forest)"/>
    </svg>
    <div class="grass" role="img" aria-label="Tuft of grass at the end of the band"
         style="background:linear-gradient(180deg,rgba(79,127,47,0) 0%,var(--forest) 45%,var(--forest) 100%)"></div>

    <p class="slogan">YOUR EVERYTHING OUTSIDE COMPANY</p>
    <p class="phone">+1 555 204 3816</p>
  </section>

  <section class="card card--back" aria-label="Card back">
    <div class="signature-line" aria-label="Space for salesman name"></div>
    <p class="tagline">At Your Convenience</p>
    <div class="service-band">
      <ul class="service-list service-list--start">
        <li>Lawn Service</li>
        <li>Pressure Washing</li>
      </ul>
      <ul class="service-list service-list--end">
        <li>Fertilization</li>
        <li>Pool Service</li>
      </ul>
    </div>
  </section>

</main>
</body>
</html>
```